Timbrafix de México
Imprimiendo Ideas
Corporate
Rodrigo Salcedo Imaz
CEO
17 de Octubre 583 Loc. B-7 Col. Pradera, Deleg. Tlalmiro, C.P. 00000
4857-3160 Vocalta
rodrigosalcedo@timbrafix-ejemplo.com.mx
ww.timbrafix-ejemplo.com.mx
Tarjetas * Postales * Volantes *
* Folders * Revistas

```html
<!DOCTYPE html>
<html lang="es">
<head>
<meta charset="utf-8">
<title>Timbrafix de México — Papelería corporativa</title>
<link href="https://fonts.googleapis.com/css2?family=Roboto:wght@400;700&display=swap" rel="stylesheet">
<style>
  :root{
    --navy:#1b2f8a;
    --red:#e0282e;
    --ink:#444;
    --paper:#ffffff;
    --ground:#e6e4e0;
    --card-black:#121212;
    --blue-hi:#2a4bc0;
    --blue-lo:#0c1a5a;
    --line:#d4d4d4;
  }
  *{box-sizing:border-box;margin:0;padding:0}
  html,body{width:1200px;height:727px;overflow:hidden;background:var(--ground);font-family:"Roboto",Arial,sans-serif}
  .canvas{position:relative;width:1200px;height:727px}
  .piece{position:absolute;background:var(--paper);box-shadow:0 2px 6px rgba(0,0,0,.18);overflow:hidden}
  .brand{display:flex;align-items:center;gap:6px}
  .brand-dot{border-radius:50%;background:var(--navy);flex:none}
  .brand-name{font-weight:700;color:var(--navy);white-space:nowrap}
  .tagline{color:var(--red);font-weight:400;white-space:nowrap}
  .small{font-size:7px;color:var(--ink);line-height:1.5;white-space:nowrap}
  .services{list-style:none;font-size:8px;line-height:1.5;color:#fff;white-space:nowrap}
  .services li::before{content:"• "}

  /* business cards */
  .card{width:180px;height:93px;padding:10px 12px}
  .card-name{top:10px;left:108px}
  .card-name .person{font-size:8px;font-weight:700;color:var(--navy);text-align:right}
  .card-name .role{font-size:7px;color:var(--red);text-align:right}
  .card-name .brand{margin-top:10px}
  .card-front{top:113px;left:29px;width:170px;height:86px}
  .card-front .services{color:var(--navy);margin:6px 0 0 64px;font-size:7px}
  .card-black{top:113px;left:206px;width:154px;height:86px;background:var(--card-black);display:flex;align-items:center;gap:12px}
  .card-blue{top:221px;left:110px;width:190px;height:103px;background:linear-gradient(135deg,var(--blue-hi),var(--blue-lo))}
  .card-blue .brand{justify-content:center;margin-top:8px}
  .card-blue .brand-name{color:#fff}
  .card-blue .brand-dot{background:#fff}
  .card-blue .services{display:flex;flex-wrap:wrap;gap:0 9px;justify-content:center;margin-top:12px}

  /* envelopes */
  .envelope-front{top:350px;left:41px;width:430px;height:260px;padding:22px}
  .envelope-front .small{margin-top:6px}
  .envelope-back{top:380px;left:490px;width:185px;height:230px;background:none}

  /* letterhead */
  .letterhead{top:77px;left:689px;width:432px;height:559px;padding:36px 34px}
  .letterhead .tagline{font-size:13px;margin-left:40px}
  .letterhead .small{margin-top:14px;font-size:7.5px}
  .letterhead .web{position:absolute;bottom:22px;left:0;right:0;text-align:center;color:var(--red);font-size:8px}
</style>
</head>
<body>
<main class="canvas">

  <section class="piece card card-name">
    <p class="person">Rodrigo Salcedo Imaz</p>
    <p class="role">CEO</p>
    <div class="brand"><span class="brand-dot" style="width:12px;height:12px"></span><span class="brand-name" style="font-size:10px">Timbrafix de México</span></div>
    <p class="small" style="margin-top:4px;font-size:6.5px">rodrigosalcedo@timbrafix-ejemplo.com.mx</p>
  </section>

  <section class="piece card card-front">
    <div class="brand"><span class="brand-dot" style="width:11px;height:11px"></span><span class="brand-name" style="font-size:9.5px">Timbrafix de México</span></div>
    <p class="tagline" style="font-size:7px;margin-left:17px">Imprimiendo Ideas</p>
    <ul class="services"><li>Tarjetas</li><li>Postales</li><li>Volantes</li></ul>
  </section>

  <section class="piece card card-black">
    <span class="brand-dot" style="width:24px;height:24px;background:#fff"></span>
    <ul class="services" style="columns:2;column-gap:10px;font-size:7px">
      <li>Tarjetas</li><li>Postales</li><li>Volantes</li><li>Folders</li><li>Revistas</li>
    </ul>
  </section>

  <section class="piece card card-blue">
    <div class="brand"><span class="brand-dot" style="width:13px;height:13px"></span><span class="brand-name" style="font-size:10.5px">Timbrafix de México</span></div>
    <ul class="services" style="font-size:7.5px"><li>Tarjetas</li><li>Postales</li><li>Volantes</li><li>Folders</li><li>Revistas</li></ul>
  </section>

  <section class="piece envelope-front">
    <div class="brand"><span class="brand-dot" style="width:16px;height:16px"></span><span class="brand-name" style="font-size:13px">Timbrafix de México</span></div>
    <p class="tagline" style="font-size:9px;margin-left:22px">Imprimiendo Ideas</p>
    <p class="small">17 de Octubre 583 Loc. B-7 Col. Pradera,<br>Deleg. Tlalmiro, C.P. 00000</p>
  </section>

  <svg class="piece envelope-back" viewBox="0 0 185 230" aria-label="Reverso del sobre">
    <rect x="0" y="0" width="185" height="230" fill="var(--paper)"/>
    <polygon points="0,0 92.5,100 185,0" fill="#f4f4f4" stroke="var(--line)"/>
    <polygon points="0,230 80,120 105,120 185,230" fill="none" stroke="var(--line)"/>
    <polygon points="22,12 92.5,86 163,12" fill="var(--card-black)"/>
    <circle cx="92.5" cy="38" r="10" fill="#fff"/>
    <text x="92.5" y="218" text-anchor="middle" font-size="6.5" font-family="Roboto, Arial, sans-serif" fill="var(--red)">ww.timbrafix-ejemplo.com.mx</text>
  </svg>

  <section class="piece letterhead">
    <div class="brand"><span class="brand-dot" style="width:22px;height:22px"></span><span class="brand-name" style="font-size:18px">Timbrafix de México</span></div>
    <p class="tagline">Imprimiendo Ideas</p>
    <p class="small">17 de Octubre 583 Loc. B-7 Col. Pradera,<br>Deleg. Tlalmiro, C.P. 00000<br>Tel. 4857-3160 Vocalta<br>rodrigosalcedo@timbrafix-ejemplo.com.mx</p>
    <p class="web">ww.timbrafix-ejemplo.com.mx</p>
  </section>

</main>
</body>
</html>
```